Larkmoor Counseling

We need a postcard design for a Brooklyn based counseling service geared towards new parents. The postcard will be placed in pediatrician's offices, kids stores, and any place parents frequent. We would like to see designs that incorporate elements, fonts, textures, etc from the website (www.larkmoorcounseling-example.com) and some of the basic text used to describe the business.

I've included a copy of the logo, the font file we used to create the logo, and the main image from the index of the website, and the background texture.

Target Market(s)

New parents in Brooklyn.

Industry/Entity Type

Business

Requirements
Must have
• Contact info, website.
Should not have
• This postcard is for display and promotional purposes in doctor's offices and kid's toy/clothing stores.

It does not need an area for postage / address.

```html
<!DOCTYPE html>
<html lang="en">
<head>
<meta charset="utf-8">
<title>Larkmoor Counseling – Postcard</title>
<link rel="stylesheet" href="https://fonts.googleapis.com/css2?family=Open+Sans:wght@300;400;600;700&display=swap">
<style>
  :root {
    --backdrop: #5f6062;
    --card: #ffffff;
    --band: #e8e6cf;
    --ink: #231f20;
    --rule: #6d6d6d;
    --street-top: #8a9a7a;
    --street-mid: #7a5a55;
    --street-low: #5e4540;
    --group-photo: #b8b4ae;
    --garden-light: #d9e2a8;
    --garden-dark: #4a4a3a;
    --portrait: #c9b8b4;
    --frame: #ffffff;
  }
  * { margin: 0; padding: 0; box-sizing: border-box; }
  html, body { width: 1200px; height: 962px; overflow: hidden; }
  body { background: var(--backdrop); font-family: "Open Sans", Arial, sans-serif; color: var(--ink); position: relative; }

  .postcard {
    position: absolute; left: 81px; top: 83px; width: 1037px; height: 795px;
    background: var(--card); overflow: hidden;
  }
  .hero-photo {
    position: absolute; left: 0; top: 0; width: 780px; height: 255px;
    background: linear-gradient(90deg, var(--street-top) 0%, var(--street-mid) 22%, var(--street-mid) 70%, var(--street-low) 100%);
  }
  .section-title {
    position: absolute; left: 39px; top: 215px;
    font-weight: 300; font-size: 42px; line-height: 1; color: #fff; letter-spacing: -0.3px;
    white-space: nowrap;
  }
  .service { position: absolute; top: 289px; width: 340px; white-space: nowrap; }
  .service--individual { left: 42px; }
  .service--group { left: 419px; }
  .service h3 { font-size: 17.5px; font-weight: 700; line-height: 22px; margin-bottom: 14px; }
  .service p { font-size: 19px; line-height: 26.2px; letter-spacing: -0.1px; }
  .service-divider { position: absolute; left: 384px; top: 290px; width: 1px; height: 184px; background: var(--rule); }

  .snapshot {
    position: absolute; background: var(--frame);
    box-shadow: 0 3px 8px rgba(0,0,0,0.35);
  }
  .snapshot--group { left: 740px; top: -60px; width: 320px; height: 265px; transform: rotate(-8deg); padding: 14px 14px 40px; }
  .snapshot--expecting { left: 752px; top: 200px; width: 290px; height: 350px; transform: rotate(-10deg); padding: 16px 16px 62px; }
  .snapshot .photo { width: 100%; height: 100%; }
  .photo--group { background: linear-gradient(160deg, #d8d6d2, var(--group-photo) 55%, #6a665f); }
  .photo--expecting { background: linear-gradient(90deg, var(--garden-light), #b9c37e 45%, var(--garden-dark) 100%); }

  .bio-band { position: absolute; left: 0; top: 512px; width: 100%; height: 283px; background: var(--band); }
  .headshot-frame { position: absolute; left: 47px; top: 28px; width: 205px; height: 222px; background: var(--frame); padding: 13px; }
  .headshot { width: 100%; height: 100%; background: linear-gradient(180deg, #e8e6e4, var(--portrait)); }
  .bio { position: absolute; left: 289px; top: 24px; width: 730px; white-space: nowrap; }
  .bio h2 { font-size: 27px; font-weight: 700; line-height: 34px; margin-bottom: 6px; }
  .bio p { font-size: 18px; line-height: 26px; letter-spacing: -0.15px; }
  .contact {
    position: absolute; left: 289px; top: 258px;
    font-size: 14px; font-weight: 600; line-height: 18px; white-space: nowrap;
  }
  .contact span + span::before { content: "·"; margin: 0 10px; }
</style>
</head>
<body>
  <main class="postcard">
    <div class="hero-photo" role="img" aria-label="Brooklyn brownstone row houses with stoops and a flowering tree"></div>
    <h1 class="section-title">Services Offered</h1>

    <section class="service service--individual">
      <h3>Individual and Couples Therapy</h3>
      <p>Individual and couples therapy<br>may focus on pregnancy<br>and postpartum depression,<br>anxiety, relationship changes,<br>confidence building, and<br>balancing work and home life.</p>
    </section>
    <div class="service-divider"></div>
    <section class="service service--group">
      <h3>Group Therapy</h3>
      <p>Larkmoor Counseling offers<br>ongoing group sessions<br>to learn and practice<br>mindfulness techniques that<br>can be used while home<br>with a baby.</p>
    </section>

    <section class="bio-band">
      <div class="headshot-frame">
        <div class="headshot" role="img" aria-label="Portrait of the therapist"></div>
      </div>
      <div class="bio">
        <h2>Nora Halvorsen, LCSW</h2>
        <p>Nora Halvorsen is a clinical social worker with over 10 years experience<br>with individual, family, and group counseling. Nora has a graduate degree<br>from BKU’s School of Social Work and psychoanalytic training from<br>The Institute for Human Growth. She has been trained in Rational<br>Emotive Behavioral Therapy and Dialectical Behavioral Therapy. Among<br>the techniques she uses is a focus on mindfulness in her work with new<br>parents. She is currently a mother of two living in Brooklyn.</p>
      </div>
      <p class="contact"><span>Brooklyn, NY</span><span>(718) 555-0142</span><span>www.larkmoorcounseling-example.com</span></p>
    </section>

    <figure class="snapshot snapshot--group">
      <div class="photo photo--group" role="img" aria-label="People seated in a circle during a group session"></div>
    </figure>
    <figure class="snapshot snapshot--expecting">
      <div class="photo photo--expecting" role="img" aria-label="Expectant mother leaning against a tree outdoors"></div>
    </figure>
  </main>
</body>
</html>
```